Lanternway Circle Monthly Giving Flyer

We need a flyer to promote a monthly giving program called Lanternway Circle to support our nonprofit organization, Brightpath Youth Trust. We have a group of students from Uganda travelling across the country in a performing arts group called Voices of Korali. While they are on tour we want audience members to sign up to become monthly donors and support our ongoing educational work in Uganda. This flyer will be on the info table, in seats, and handed out throughout the course of the tour.

Lanternway Circle is a new program. The idea is that the audience members will be motivated by their interaction with the students to fill in their information to sign up to make a monthly gift. In exchange, we'll give them a free merchandise item (CD, tshirt, etc) for signing up and we'll send them special updates from the students throughout the year electronically.

Check out BrightpathYouthTrust.org for more info about our programs, Lanternway Circle and our branding/style.

This will be printed as a 5x7 two-sided postcard that we can print cheaply in color.

Side 1: Draw attention to the program graphically with a message of "Join Us Become an Lanternway Member," happy student image, etc. You can download an image from the gallery on our website, if you choose at: http://www.brightpathyouthtrust.org/who-we-are/media/ (scroll to the bottom)

Side 2: Lead in text: Join our network of friends committed to supporting the ongoing education of Brightpath scholars through monthly donations. As an Lanternway Member, you play a critical role by helping ensure that we can provide the life-changing services to our scholars month in and month out.
We'll send you special updates from the students throughout the year to keep you up to date on how your gifts are impacting lives.

I'd like to give $25, $50, $75, $100, or $____ other amount
Name, address, phone number, email
Credit card #, expiration, and security code
I've provided a voided check for monthly electronic funds transfer

Requirements
Nice to have
• We have not created a logo or done any branding for Lanternway Circle so it would be nice to have a nicely designed logo/font for Lanternway Circle incorporated into the flyer design that we can in other places as well to promote the program.
Should not have
• Anything that play on the poverty or challenges in Africa. We try to provide always positive image of Africa and the students we work with.

```html
<!DOCTYPE html>
<html lang="en">
<head>
<meta charset="utf-8">
<title>Lanternway Circle Monthly Giving Card</title>
<link href="https://fonts.googleapis.com/css2?family=Arimo:wght@400;700&display=swap" rel="stylesheet">
<style>
  :root {
    --orange-deep: #f08a2c;
    --orange-mid: #f6a85a;
    --orange-light: #fbd0a3;
    --peach-pale: #fdebd9;
    --peach-warm: #f9c28b;
    --ink: #2a2420;
    --white: #ffffff;
  }
  * { margin: 0; padding: 0; box-sizing: border-box; }
  html, body { width: 857px; height: 1200px; overflow: hidden; }
  body { font-family: "Arimo", Arial, sans-serif; background: var(--white); }

  .card { position: relative; width: 857px; height: 1200px; overflow: hidden; }

  .intro {
    position: absolute; left: 0; top: 0; width: 857px; height: 480px;
    background: radial-gradient(ellipse 75% 95% at 50% 40%, var(--orange-light) 0%, var(--orange-mid) 45%, var(--orange-deep) 100%);
    color: var(--white);
    text-align: center;
    padding: 42px 120px 0;
    font-size: 25px; line-height: 1.2;
  }
  .intro p { margin-bottom: 30px; }

  .divider-glow {
    position: absolute; left: 0; top: 440px; width: 857px; height: 110px;
    background: radial-gradient(ellipse 55% 40% at 50% 35%, rgba(120,60,10,0.35) 0%, rgba(120,60,10,0) 70%);
  }

  .pledge {
    position: absolute; left: 0; top: 480px; width: 857px; height: 720px;
    background: linear-gradient(180deg, var(--peach-pale) 0%, var(--peach-pale) 25%, var(--peach-warm) 75%, var(--orange-mid) 100%);
    color: var(--ink);
    font-size: 22px;
  }

  .pledge-title { position: absolute; left: 80px; top: 170px; font-weight: 700; font-size: 24px; }

  .amounts { position: absolute; left: 80px; top: 235px; display: flex; gap: 0; }
  .amount { display: flex; align-items: center; width: 176px; }
  .box { width: 18px; height: 18px; border: 2px solid var(--ink); margin-right: 22px; }

  .field { position: absolute; white-space: nowrap; }
  .leader { display: inline-block; height: 4px; border-bottom: 3px dotted var(--ink); margin-left: 6px; vertical-align: baseline; }
</style>
</head>
<body>
<div class="card">
  <section class="intro">
    <p>Join our network of friends committed to supporting the ongoing education of Brightpath scholars through monthly donations.</p>
    <p>As an Lanternway Member, you play a critical role by helping ensure that we can provide the life-changing services to our scholars month in and month out.</p>
    <p>We’ll send you special updates from the students throughout the year to keep you up to date on how your gifts are impacting lives.</p>
  </section>
  <div class="divider-glow"></div>

  <section class="pledge">
    <h2 class="pledge-title">I would like to give:</h2>
    <div class="amounts">
      <div class="amount"><span class="box"></span>$25</div>
      <div class="amount"><span class="box"></span>$50</div>
      <div class="amount"><span class="box"></span>$75</div>
      <div class="amount"><span class="box"></span>$100</div>
    </div>

    <div class="field" style="left:80px; top:305px;">Other amount: <span class="leader" style="width:230px"></span></div>

    <div class="field" style="left:80px; top:365px;">Name: <span class="leader" style="width:195px"></span></div>
    <div class="field" style="left:80px; top:398px;">Address: <span class="leader" style="width:170px"></span></div>
    <div class="field" style="left:80px; top:431px;"><span class="leader" style="width:262px; margin-left:0"></span></div>

    <div class="field" style="left:429px; top:365px;">Credit Card #: <span class="leader" style="width:200px"></span></div>
    <div class="field" style="left:429px; top:398px;">Expiration: <span class="leader" style="width:232px"></span></div>
    <div class="field" style="left:429px; top:431px;">Security Code: <span class="leader" style="width:200px"></span></div>

    <div class="field" style="left:80px; top:500px;">Phone no: <span class="leader" style="width:160px"></span></div>
    <div class="field" style="left:80px; top:533px;">Email: <span class="leader" style="width:195px"></span></div>

    <div class="field" style="left:80px; top:590px;">I’ve provided a voided check for monthly electronic funds transfer.</div>
    <div class="field" style="left:80px; top:628px;">Check details: <span class="leader" style="width:230px"></span></div>
  </section>
</div>
</body>
</html>
```